May/June Newsletter

We require a newsletter with as much infographic as possible

Attached is our previous newsletter as an example.

ONLY USE THE DATA IN EPC CHALLENGES

Target Market(s)

property market

Requirements
Must have
• Company colours and logo from
www.velmarkhub.co.uk

be similar to our previous newsletter. copy attached.

must have a screenshot of VHDigital attached

```html
<!DOCTYPE html>
<html lang="en">
<head>
<meta charset="utf-8">
<title>Velmark Hub – EPC Challenges Newsletter</title>
<link href="https://fonts.googleapis.com/css2?family=Montserrat:wght@600;700&family=Open+Sans:wght@400;600;700&display=swap" rel="stylesheet">
<style>
:root{
  --page:#eeeced;
  --card:#ffffff;
  --teal:#1a9a8a;
  --teal-light:#3ec9b6;
  --text:#555555;
  --muted:#777777;
  --rule:#d9d9d9;
  --link:#d0262e;
  --green:#8bc34a;
  --dark:#3a3a3a;
}
*{margin:0;padding:0;box-sizing:border-box}
html,body{width:1200px;height:3710px;overflow:hidden;background:var(--page)}
body{font-family:"Open Sans",Arial,sans-serif;color:var(--text);position:relative}
.preheader{position:absolute;top:68px;left:0;width:1200px;text-align:center;font-family:Arial,Helvetica,sans-serif;font-size:20px;color:#444;line-height:26px}
.preheader a{color:var(--link);text-decoration:underline}
.card{position:absolute;left:232px;top:150px;width:738px;height:3448px;background:var(--card);border-radius:18px}
.content{position:absolute;left:29px;width:680px}
.brand{font-family:"Open Sans",Arial,sans-serif;font-weight:700;font-size:34px;color:var(--dark);letter-spacing:1px;display:flex;align-items:center;gap:10px}
.brand-dot{width:24px;height:24px;border-radius:50%;background:var(--teal)}
.header{top:44px;height:62px;display:flex;justify-content:space-between;align-items:center}
.header-mail{display:flex;align-items:center;gap:10px;font-size:17px;color:var(--muted)}
.icon-circle{width:38px;height:38px;border:2px solid #888;border-radius:50%;display:flex;align-items:center;justify-content:center}
.hero{top:133px;height:369px;background:linear-gradient(135deg,#12897b 0%,var(--teal-light) 100%);overflow:hidden}
.hero-title{position:absolute;left:32px;top:62px;font-family:Montserrat,Arial,sans-serif;font-weight:700;font-size:36px;line-height:45px;color:#fff}
.hero-btn{position:absolute;left:33px;top:267px;width:212px;height:51px;background:var(--green);color:#fff;font-family:Montserrat,Arial,sans-serif;font-weight:600;font-size:17px;display:flex;align-items:center;justify-content:center}
.hero-art{position:absolute;left:325px;top:48px;width:342px;height:277px;border-radius:8px;background:linear-gradient(180deg,rgba(255,255,255,.25) 0%,rgba(255,255,255,.1) 65%,#6aa63a 80%,#4f8f2e 100%)}
.section-title{font-family:Montserrat,Arial,sans-serif;font-weight:700;font-size:30px;color:var(--teal);line-height:36px}
.date-head{display:flex;align-items:center;gap:12px;font-family:Montserrat,Arial,sans-serif;font-weight:700;font-size:23px;color:var(--teal);line-height:28px}
.body-text{font-size:18.5px;line-height:30px}
.body-text p+p{margin-top:30px}
.narrow{width:430px}
.rule{height:2px;background:var(--rule)}
.earth-art{left:509px;top:911px;width:200px;height:320px;border-radius:8px;background:linear-gradient(180deg,#6f8ea8 0%,#34495c 40%,#2a2a2a 70%,#5a5a5a 90%,#f2f2f2 100%)}
.epc-scale{top:1620px;width:320px;height:358px}
.house-art{left:393px;top:1618px;width:283px;height:327px;border-radius:8px;background:linear-gradient(180deg,#8cc63f 0%,#b9d27a 30%,#efe7d0 55%,#e4d9bd 100%)}
.read-more{font-weight:700;font-size:16px;color:var(--teal);text-decoration:none}
.tool-figure{top:2413px;left:111px;width:475px;height:520px;border-radius:6px;background:linear-gradient(180deg,#f2f2f2 0%,#cfcfcf 55%,#bfe3f2 80%,#f2f2f2 100%)}
.footer-social{display:flex;gap:11px;margin-top:14px}
.social{width:40px;height:40px;border:2px solid var(--dark);border-radius:50%}
.contact{left:393px;width:300px}
.contact-title{font-family:Montserrat,Arial,sans-serif;font-weight:700;font-size:17px;color:var(--teal);letter-spacing:.5px}
.contact-item{display:flex;gap:12px;font-size:17px;line-height:27px;color:var(--text);margin-top:14px}
.contact-item svg{flex:none;margin-top:4px}
.copyright{top:3376px;left:0;width:738px;text-align:center;font-size:17px;color:var(--text)}
</style>
</head>
<body>
<div class="preheader">Is this email not displaying correctly?<br><a href="#">View it in your browser.</a></div>

<main class="card">
  <header class="content header">
    <div class="brand"><span>VELMARK HUB</span><span class="brand-dot"></span></div>
    <div class="header-mail">
      <span class="icon-circle"><svg width="18" height="14" viewBox="0 0 18 14"><rect x="1" y="1" width="16" height="12" fill="none" stroke="#888" stroke-width="1.6"/><path d="M1 1l8 7 8-7" fill="none" stroke="#888" stroke-width="1.6"/></svg></span>
      info@velmarkhub.co.uk
    </div>
  </header>

  <section class="content hero">
    <h1 class="hero-title">ENERGY<br>PERFORMANCE<br>IMPROVEMENT<br>SERVICES</h1>
    <a class="hero-btn">GET IN TOUCH</a>
    <div class="hero-art" role="img" aria-label="Illustration of two wind turbines on a green hill"></div>
  </section>

  <h2 class="content section-title" style="top:522px">EPC CHALLENGES</h2>
  <h3 class="content date-head" style="top:565px">
    <svg width="24" height="24" viewBox="0 0 24 24"><rect x="2" y="4" width="20" height="18" fill="none" stroke="#1a9a8a" stroke-width="2"/><path d="M2 9h20M7 1v5M17 1v5M6 13h3M11 13h3M16 13h3M6 17h3M11 17h3" stroke="#1a9a8a" stroke-width="2"/></svg>
    April 2023
  </h3>
  <div class="content body-text" style="top:606px">
    <p>From April 2023 existing MEES regulations will be extended to cover all non-domestic tenancies (already in place for domestic tenancies since 1st April 2020).</p>
    <p>MEES (Minimum Energy Efficiency Standard) regulations make it unlawful to agree a new lease on a property with an EPC rating below an E unless an exemption has been put in place on the PRS register.</p>
  </div>
  <div class="content rule" style="top:829px"></div>

  <h3 class="content date-head" style="top:889px">
    <svg width="24" height="24" viewBox="0 0 24 24"><rect x="2" y="4" width="20" height="18" fill="none" stroke="#1a9a8a" stroke-width="2"/><path d="M2 9h20M7 1v5M17 1v5M6 13h3M11 13h3M16 13h3M6 17h3M11 17h3" stroke="#1a9a8a" stroke-width="2"/></svg>
    Beyond April 2023
  </h3>
  <div class="content earth-art" role="img" aria-label="Illustration of the Earth crumbling into a pile of coal"></div>
  <div class="content body-text" style="top:922px">
    <p class="narrow">The UK Governments long term aim of having net zero carbon emissions by 2050 has several key dates before to make this achievable.</p>
    <p class="narrow">Consultation process closed in January this year into the minimum energy standards for non domestic properties. The consultation process looked into the future trajectory of measures up to 2030, with one suggestion being for commercial properties to be of minimum band C or B.</p>
    <p>The Clean Growth Strategy is already in place to help as many domestic properties achieve band C by 2035.<br>The definition is two-pronged. Firstly, during the construction process of an asset, the amount of carbon emissions produced should be zero, or negative through the use of offsets or the export of on-site renewable energy. Secondly, during the use of the building, the amount of carbon emissions produced from the building's operational energy should also be zero or negative.</p>
  </div>
  <div class="content rule" style="top:1505px"></div>

  <h3 class="content date-head" style="top:1566px">Ongoing</h3>
  <svg class="content epc-scale" viewBox="0 0 320 358" role="img" aria-label="EPC rating scale A to G">
    <g font-family="Open Sans, Arial, sans-serif" font-size="24" fill="#fff">
      <polygon points="0,0 80,0 100,19 80,38 0,38" fill="#2e7d1a"/><text x="8" y="28">A</text>
      <polygon points="0,51 120,51 140,70 120,89 0,89" fill="#68a81e"/><text x="8" y="79">B</text>
      <polygon points="0,102 152,102 172,121 152,140 0,140" fill="#b9d82a"/><text x="8" y="130">C</text>
      <polygon points="0,153 188,153 208,172 188,191 0,191" fill="#e3b62a"/><text x="8" y="181">D</text>
      <polygon points="0,204 223,204 243,223 223,242 0,242" fill="#e0841a"/><text x="8" y="232">E</text>
      <polygon points="0,255 256,255 276,274 256,293 0,293" fill="#d24f18"/><text x="8" y="283">F</text>
      <polygon points="0,306 289,306 309,325 289,344 0,344" fill="#cc1616"/><text x="8" y="334">G</text>
    </g>
  </svg>
  <div class="content house-art" role="img" aria-label="Illustration of a house with a green roof"></div>
  <div class="content body-text" style="top:2012px">
    <p>From April 2023 existing MEES regulations will be extended to cover all non-domestic tenancies (already in place for domestic tenancies since 1st April 2020).</p>
    <p>MEES (Minimum Energy Efficiency Standard) regulations make it unlawful to agree a new lease on a property with an EPC rating below an E unless an exemption has been put in place on the PRS register.</p>
  </div>
  <a class="content read-more" style="top:2228px">Read More &gt;</a>
  <div class="content rule" style="top:2294px"></div>

  <div class="content body-text" style="top:2321px">
    <p>Velmark Hub have developed a market leading EPC management tool to meet the current and ongoing EPC challenges faced in the property market.</p>
  </div>
  <div class="content tool-figure" role="img" aria-label="Illustration of a warehouse with two screens comparing its previous band D rating and current band E rating over a 10 year span"></div>
  <div class="content body-text" style="top:2978px">
    <p>We are currently offering free trials on VHDigital to demonstrate how we can assist to manage the above challenges.</p>
  </div>
  <div class="content rule" style="top:3123px"></div>

  <footer>
    <div class="content" style="top:3172px;width:340px">
      <div class="brand" style="font-size:30px"><span>VELMARK HUB</span></div>
      <div class="footer-social"><span class="social"></span><span class="social"></span></div>
    </div>
    <div class="content contact" style="top:3168px">
      <h4 class="contact-title">CONTACT DETAILS</h4>
      <div class="contact-item"><svg width="20" height="18" viewBox="0 0 20 18"><path d="M10 1L1 9h3v8h4v-5h4v5h4V9h3z" fill="#666"/></svg>Velmark Hub Limited</div>
      <div class="contact-item"><svg width="16" height="20" viewBox="0 0 16 20"><path d="M8 1a6 6 0 0 0-6 6c0 5 6 12 6 12s6-7 6-12a6 6 0 0 0-6-6z" fill="none" stroke="#666" stroke-width="1.6"/><circle cx="8" cy="7" r="2" fill="#666"/></svg>Larkfield House, 48-52 Tannery Lane, London, EC2R 4QT</div>
      <div class="contact-item"><svg width="18" height="14" viewBox="0 0 18 14"><rect x="1" y="1" width="16" height="12" fill="none" stroke="#666" stroke-width="1.6"/><path d="M1 1l8 7 8-7" fill="none" stroke="#666" stroke-width="1.6"/></svg>info@velmarkhub.co.uk</div>
    </div>
    <p class="content copyright">Copyright Velmark Hub Limited - All rights reserved ©2016.</p>
  </footer>
</main>
</body>
</html>
```